Design and Renovation Company Luxury Business Card

I want to create a luxury business card for a Design and Renovation Firm . We will use our current logo. The company name is 742BUILD. We do not want anything standard. We need a very unique concept.
Please see uploaded inspiration. I really like the textured paper option. I would like the card to be thick with debossing, and/or embossing options. The logo has orange in it but I would like to see the card with and without the orange. I think the orange may make the company feel less high-end. The goal is to elevate the logo not match its vibe per se of the logo. We want something very unique, not standard at all!
I would like a space for :
Logo,
Name,
Position,
Email,
Office number,
Website Address,
Business Address,
Thank you!
Have fun!
Target Market(s)
Home owners Age 35 +
Industry/Entity Type
Design and Renovation
Contact Information for Business Card
Logo, Name, Position, Email, Office number, Website Address, Business Address,.
Colors
Designer to choose colors to be used in the design.
Requirements
Must have
- A luxury designer feel. Must be black or dark grey but open to other luxury ideas.
Nice to have
- Gold, silver, black embossing or debossing. Textured paper design.
Should not have
- A cheap look and feel.

```html
<!DOCTYPE html>
<html lang="en">
<head>
<meta charset="utf-8">
<title>742BUILD Business Card</title>
<link rel="stylesheet" href="https://fonts.googleapis.com/css2?family=Montserrat:wght@500;600&display=swap">
<style>
  :root {
    --backdrop: #4d4d4e;
    --card: #1d1d21;
    --card-edge: #26262b;
    --copper: #a9631f;
    --copper-dim: #8f5419;
  }
  * { margin: 0; padding: 0; box-sizing: border-box; }
  html, body {
    width: 1200px; height: 1200px; overflow: hidden;
    background: var(--backdrop);
    font-family: "Montserrat", sans-serif;
  }
  .canvas { position: relative; width: 1200px; height: 1200px; }
  .card {
    position: absolute; left: 303px; width: 700px; height: 438px;
    background: var(--card);
    border-radius: 8px;
    box-shadow: 0 10px 22px rgba(0,0,0,.35), inset 0 0 0 1px var(--card-edge);
  }
  .card--front { top: 151px; }
  .card--back { top: 672px; }

  /* Front */
  .brand {
    position: absolute; left: 0; right: 0; top: 186px;
    display: flex; flex-direction: column; align-items: center;
  }
  .brand__row { display: flex; align-items: center; gap: 14px; }
  .brand__square { width: 34px; height: 34px; background: var(--copper); }
  .brand__name {
    color: var(--copper); font-weight: 500; font-size: 42px;
    letter-spacing: 5px; line-height: 1;
  }
  .brand__tagline {
    margin-top: 6px; color: var(--copper); font-weight: 500;
    font-size: 11px; letter-spacing: 3.6px; padding-left: 48px;
  }

  /* Back */
  .badge {
    position: absolute; left: 503px; top: 60px;
    display: flex; flex-direction: column; align-items: center; gap: 16px;
  }
  .badge__square { width: 116px; height: 116px; background: var(--copper); }
  .badge__name {
    color: var(--copper); font-weight: 500; font-size: 20px;
    letter-spacing: 2.5px; line-height: 1;
  }
  .person { position: absolute; left: 68px; top: 286px; color: var(--copper); }
  .person__name { font-weight: 600; font-size: 22px; line-height: 1; }
  .person__title { font-weight: 500; font-size: 15px; color: var(--copper-dim); margin-top: 3px; line-height: 1; }
  .rule {
    position: absolute; left: 68px; top: 338px; width: 568px; height: 1.5px;
    background: var(--copper);
  }
  .contact {
    position: absolute; list-style: none; color: var(--copper);
    font-weight: 500; font-size: 17px; line-height: 1;
  }
  .contact li { display: flex; align-items: flex-start; gap: 9px; }
  .contact svg { flex: none; fill: var(--copper); }
  .contact--left { left: 68px; top: 356px; }
  .contact--left li + li { margin-top: 14px; }
  .contact--right { left: 428px; top: 348px; font-size: 15.5px; }
  .contact--right li + li { margin-top: 12px; }
  .contact__address { line-height: 1.25; }
</style>
</head>
<body>
<main class="canvas">
  <section class="card card--front">
    <div class="brand">
      <div class="brand__row">
        <span class="brand__square"></span>
        <span class="brand__name">742BUILD</span>
      </div>
      <span class="brand__tagline">Design and Renovation Firm</span>
    </div>
  </section>

  <section class="card card--back">
    <div class="badge">
      <span class="badge__square"></span>
      <span class="badge__name">742BUILD</span>
    </div>
    <div class="person">
      <p class="person__name">FULL NAME</p>
      <p class="person__title">TITLE</p>
    </div>
    <div class="rule"></div>
    <ul class="contact contact--left">
      <li>
        <svg width="20" height="20" viewBox="0 0 24 24" aria-hidden="true"><path d="M6.6 10.8a15 15 0 0 0 6.6 6.6l2.2-2.2a1 1 0 0 1 1-.25 11.4 11.4 0 0 0 3.6.57 1 1 0 0 1 1 1V20a1 1 0 0 1-1 1A17 17 0 0 1 3 4a1 1 0 0 1 1-1h3.5a1 1 0 0 1 1 1c0 1.25.2 2.45.57 3.57a1 1 0 0 1-.25 1z"/></svg>
        <span>(000) 000 0000</span>
      </li>
      <li>
        <svg width="22" height="18" viewBox="0 0 24 18" aria-hidden="true"><path d="M1 1h22v16H1z M3 3v.6l9 6 9-6V3z M3 6v9h18V6l-9 6z" fill-rule="evenodd"/></svg>
        <span>email@company.com</span>
      </li>
    </ul>
    <ul class="contact contact--right">
      <li>
        <svg width="18" height="18" viewBox="0 0 24 24" aria-hidden="true"><path fill="none" stroke="#a9631f" stroke-width="1.8" d="M12 2a10 10 0 1 0 0 20 10 10 0 0 0 0-20zM2 12h20M12 2c3 3 3 17 0 20M12 2c-3 3-3 17 0 20M4 7h16M4 17h16"/></svg>
        <span>www.company.com</span>
      </li>
      <li>
        <svg width="16" height="22" viewBox="0 0 16 22" aria-hidden="true"><path d="M8 0a8 8 0 0 0-8 8c0 6 8 14 8 14s8-8 8-14a8 8 0 0 0-8-8zm0 11a3 3 0 1 1 0-6 3 3 0 0 1 0 6z"/></svg>
        <span class="contact__address">123 Name Street, 000<br>Your City, 00000-000</span>
      </li>
    </ul>
  </section>
</main>
</body>
</html>
```